Business Card Design for Bright Easel Designs

I need a business card design for Artist Marlon Teague who specializes in Digital Fine Art, Digital Illustration, Murals and Mixed Media. Digital art techniques combine the use of a computer and specialized programs coupled with the same methods and theories used to produce traditional art. The final design should use the new logo that was just deigned and reflect an artist who has embraced the evolution of art by using modern technology to paint vibrant, stunning and high quality art. Please make this a double sided card and use the attached photo on the back of the card. Please include the name of the business: Bright Easel Designs, Artist: Marlon Teague, Phone: 555-872-3096 Website: brighteaseldesigns.example

Target Market(s)

Anyone looking for fine art for there home or business.

Industry/Entity Type

Computer

Contact Information for Business Card

This should be a double sided business card with a modern feel to it.

Font styles to use
Sans Serif

Requirements
Must have
• Artist Name: Marlon Teague
• Business Name and Logo: Bright Easel Designs
• Phone: 555-872-3096
• Website: brighteaseldesigns.example
• specializes in Digital Fine Art, Digital Illustration, Murals and Mixed Media
Nice to have
• Black background with new logo that is attached to file

```html
<!DOCTYPE html>
<html lang="en">
<head>
<meta charset="utf-8">
<title>Bright Easel Designs – Business Card</title>
<link rel="stylesheet" href="https://fonts.googleapis.com/css2?family=Open+Sans:wght@400;600;700&family=Exo+2:wght@600&display=swap">
<style>
  :root {
    --backdrop: #e7e5e1;
    --card-white: #ffffff;
    --card-shade: #e4e4e6;
    --navy: #0f1f8f;
    --cyan: #1fd3f4;
    --brand-blue: #1c2f9e;
    --text-dark: #333538;
    --icon-dark: #3a3c40;
  }
  * { margin: 0; padding: 0; box-sizing: border-box; }
  html, body {
    width: 1200px;
    height: 899px;
    overflow: hidden;
    background: var(--backdrop);
  }
  .canvas {
    position: relative;
    width: 1200px;
    height: 899px;
  }
  .card {
    position: absolute;
    left: 100px;
    top: 163px;
    width: 1000px;
    height: 572px;
    overflow: hidden;
    background: radial-gradient(ellipse at 45% 55%, var(--card-white) 0%, #f6f6f7 45%, var(--card-shade) 100%);
    box-shadow: 0 14px 30px rgba(0,0,0,0.22);
  }
  .card__waves {
    position: absolute;
    inset: 0;
    width: 1000px;
    height: 572px;
  }
  .brand {
    position: absolute;
    left: 90px;
    top: 34px;
    display: flex;
    flex-direction: column;
    align-items: flex-start;
    gap: 14px;
  }
  .brand__mark {
    width: 84px;
    height: 84px;
    border-radius: 50%;
    background: var(--cyan);
    margin-left: 60px;
  }
  .brand__name {
    font-family: "Exo 2", sans-serif;
    font-weight: 600;
    font-size: 29px;
    color: var(--brand-blue);
    white-space: nowrap;
  }
  .contact {
    position: absolute;
    left: 58px;
    top: 218px;
    list-style: none;
    font-family: "Open Sans", sans-serif;
    font-size: 17px;
    line-height: 24px;
    color: var(--text-dark);
  }
  .contact__item {
    display: flex;
    align-items: flex-start;
    gap: 8px;
  }
  .contact__icon {
    flex: none;
    width: 15px;
    height: 15px;
    margin-top: 4px;
  }
  .person {
    position: absolute;
    right: 150px;
    bottom: 40px;
    text-align: right;
    font-family: "Open Sans", sans-serif;
    color: var(--text-dark);
  }
  .person__name {
    font-weight: 700;
    font-size: 37px;
    line-height: 1.15;
  }
  .person__title {
    font-weight: 400;
    font-size: 32px;
    line-height: 1.2;
  }
</style>
</head>
<body>
<main class="canvas">
  <section class="card" aria-label="Business card front">
    <svg class="card__waves" viewBox="0 0 1000 572" aria-hidden="true">
      <path d="M470 0 C700 80 880 250 1000 470 L1000 0 Z" fill="var(--cyan)"/>
      <path d="M575 0 C770 75 910 200 1000 300 L1000 0 Z" fill="var(--navy)"/>
      <path d="M790 120 C870 180 945 270 1000 340" fill="none" stroke="var(--cyan)" stroke-width="8"/>
    </svg>

    <div class="brand">
      <span class="brand__mark"></span>
      <span class="brand__name">Bright Easel Designs</span>
    </div>

    <ul class="contact">
      <li class="contact__item">
        <svg class="contact__icon" viewBox="0 0 16 16"><circle cx="8" cy="8" r="8" fill="var(--icon-dark)"/><path d="M4 8.5 L8 4.5 L12 8.5 M5.5 8 V12 H10.5 V8" fill="none" stroke="#fff" stroke-width="1.4"/></svg>
        <span>Suite # 118, Oak Bldg,<br>NY 10000</span>
      </li>
      <li class="contact__item">
        <svg class="contact__icon" viewBox="0 0 16 16"><circle cx="8" cy="8" r="8" fill="var(--icon-dark)"/><path d="M5 4.5 C5 9 7 11 11.5 11.5 L11.5 9.5 L9.5 9 L8.8 10 C7.5 9.3 6.7 8.5 6 7.2 L7 6.5 L6.5 4.5 Z" fill="#fff"/></svg>
        <span>555-872-3096</span>
      </li>
      <li class="contact__item">
        <svg class="contact__icon" viewBox="0 0 16 16"><circle cx="8" cy="8" r="8" fill="var(--icon-dark)"/><rect x="5.5" y="3.5" width="5" height="9" rx="1" fill="#fff"/><rect x="6.5" y="5" width="3" height="5" fill="var(--icon-dark)"/></svg>
        <span>555-872-3097</span>
      </li>
      <li class="contact__item">
        <svg class="contact__icon" viewBox="0 0 16 16"><circle cx="8" cy="8" r="8" fill="var(--icon-dark)"/><rect x="4" y="6" width="8" height="5.5" fill="#fff"/><rect x="5.5" y="3.5" width="5" height="2.5" fill="#fff"/></svg>
        <span>555-872-3098</span>
      </li>
      <li class="contact__item">
        <svg class="contact__icon" viewBox="0 0 16 16"><circle cx="8" cy="8" r="8" fill="var(--icon-dark)"/><rect x="4" y="5" width="8" height="6" fill="#fff"/><path d="M4 5 L8 8.5 L12 5" fill="none" stroke="var(--icon-dark)" stroke-width="1"/></svg>
        <span>name@brighteaseldesigns.example</span>
      </li>
      <li class="contact__item">
        <svg class="contact__icon" viewBox="0 0 16 16"><circle cx="8" cy="8" r="8" fill="var(--icon-dark)"/><circle cx="8" cy="8" r="4.5" fill="none" stroke="#fff" stroke-width="1"/><path d="M3.5 8 H12.5 M8 3.5 V12.5" stroke="#fff" stroke-width="1"/></svg>
        <span>www.brighteaseldesigns.example</span>
      </li>
    </ul>

    <div class="person">
      <p class="person__name">Marlon Teague</p>
      <p class="person__title">Owner / C.E.O</p>
    </div>
  </section>
</main>
</body>
</html>
```